Harlow Ridge Partners Business Cards

Design Business cards in a format where I can change the information and utilize a third party buisness card printing company

Contact Information for Business Card

Want Logo and Name on Back. Looking for Spot UV style shine on Logo. Probably Black background. Want smaller logo on front with contact details. Like rounded edges or something else interesting.

Requirements
Must have
• Strong masculine look.

```html
<!DOCTYPE html>
<html lang="en">
<head>
<meta charset="utf-8">
<title>Harlow Ridge Partners – Business Cards</title>
<link rel="stylesheet" href="https://fonts.googleapis.com/css2?family=Cinzel:wght@400;600&family=Crimson+Text:wght@400&display=swap">
<style>
  :root {
    --backdrop: #3b3b3b;
    --card: #131313;
    --card-edge: #1c1c1c;
    --ink: #ffffff;
    --ink-soft: #d9d9d9;
    --band-light: #6a6a6a;
    --band-dark: #2a2a2a;
  }
  * { margin: 0; padding: 0; box-sizing: border-box; }
  html, body { width: 799px; height: 1200px; overflow: hidden; }
  body {
    background: var(--backdrop);
    display: flex;
    flex-direction: column;
    align-items: center;
    justify-content: center;
    gap: 90px;
    font-family: "Crimson Text", Georgia, serif;
    color: var(--ink);
  }
  .card {
    position: relative;
    width: 680px;
    height: 389px;
    border-radius: 30px;
    background: var(--card);
    border: 1px solid var(--card-edge);
    overflow: hidden;
  }

  /* Front */
  .front-decoration {
    position: absolute;
    inset: 30px 60px 30px 40px;
    border-radius: 8px;
    background: linear-gradient(160deg, var(--band-dark) 0%, #1a1a1a 40%, var(--band-light) 100%);
  }
  .front-name {
    position: absolute;
    left: 0; right: 0;
    top: 150px;
    text-align: center;
    font-family: "Cinzel", "Times New Roman", serif;
    font-weight: 600;
    font-size: 44px;
    letter-spacing: 1px;
    line-height: 1.1;
    color: var(--ink);
  }

  /* Back */
  .edge-curve {
    position: absolute;
    left: 0; top: 18px;
    width: 22px; height: 60px;
  }
  .holder {
    position: absolute;
    left: 52px; top: 32px;
  }
  .holder-name {
    font-family: "Cinzel", "Times New Roman", serif;
    font-weight: 600;
    font-size: 26px;
    letter-spacing: 1px;
  }
  .holder-title {
    font-size: 15px;
    color: var(--ink-soft);
  }
  .contact {
    position: absolute;
    left: 30px; top: 210px;
    width: 300px;
    font-size: 15px;
    line-height: 1.4;
    color: var(--ink-soft);
    list-style: none;
  }
  .contact .address { margin-bottom: 10px; }
  .contact li { display: flex; align-items: center; gap: 10px; white-space: nowrap; }
  .contact svg { width: 14px; height: 14px; flex: none; }
  .brand {
    position: absolute;
    right: 44px; bottom: 70px;
    display: flex;
    align-items: center;
    gap: 14px;
  }
  .brand-mark {
    width: 16px; height: 16px;
    background: var(--ink);
    flex: none;
  }
  .brand-name {
    font-family: "Cinzel", "Times New Roman", serif;
    font-weight: 600;
    font-size: 30px;
    line-height: 1.15;
    letter-spacing: 1px;
    color: var(--ink);
  }
</style>
</head>
<body>

  <section class="card card-front">
    <div class="front-decoration" role="img" aria-label="Large glossy angled band decoration in dark and mid grey"></div>
    <h1 class="front-name">Harlow Ridge<br>Partners</h1>
  </section>

  <section class="card card-back">
    <svg class="edge-curve" viewBox="0 0 22 60" aria-hidden="true">
      <path d="M0 0 Q22 30 0 60 Z" fill="#ffffff"/>
    </svg>

    <div class="holder">
      <div class="holder-name">Dalton Reeves</div>
      <div class="holder-title">Managing Director</div>
    </div>

    <ul class="contact">
      <li class="address">88 Ridgeline Ave., Brookhollow,<br>Westfield, US 604218</li>
      <li>
        <svg viewBox="0 0 16 16" aria-hidden="true"><path d="M3 1h3l1 4-2 1c1 2 3 4 5 5l1-2 4 1v3c0 1-1 2-2 2C7 15 1 9 1 3c0-1 1-2 2-2z" fill="#ffffff"/></svg>
        (415) 555-0182
      </li>
      <li>
        <svg viewBox="0 0 16 16" aria-hidden="true"><rect x="1" y="3" width="14" height="10" fill="#ffffff"/><path d="M1 3l7 6 7-6" fill="none" stroke="#131313" stroke-width="1.3"/></svg>
        dalton@harlowridgepartners.com
      </li>
      <li>
        <svg viewBox="0 0 16 16" aria-hidden="true"><circle cx="8" cy="8" r="6.5" fill="none" stroke="#ffffff" stroke-width="1.3"/><ellipse cx="8" cy="8" rx="2.8" ry="6.5" fill="none" stroke="#ffffff" stroke-width="1"/><path d="M1.5 8h13" stroke="#ffffff" stroke-width="1"/></svg>
        www.harlowridgepartners.com
      </li>
    </ul>

    <div class="brand">
      <span class="brand-mark"></span>
      <span class="brand-name">Harlow Ridge<br>Partners</span>
    </div>
  </section>

</body>
</html>
```